New website for an SEO training system

We need a web design for an SEO company offering a Rank Ladder Kit product which is a system or recipe on how to do SEO on your blog. It's a bit like, "28 Mornings for Sharper Writing Habits" in that they it is chunked down to what should be done on a daily basis over a 30 day period. It's not so much a training product but a recipe book.
The materials are video and support docs, like to do lists and checklists. It needs to be fresh and clean, with modern design.

Target Market(s)

Bloggers

Industry/Entity Type

It Company

Font styles to use
Sans Serif

```html
<!DOCTYPE html>
<html lang="en">
<head>
<meta charset="utf-8">
<title>Rank Ladder Kit</title>
<link href="https://fonts.googleapis.com/css2?family=Raleway:wght@400;500;600&family=Open+Sans:wght@400;600&display=swap" rel="stylesheet">
<style>
:root{
  --teal:#3f8c88;
  --teal-dark:#1b4f50;
  --teal-light:#8cc2bf;
  --orange:#d56f27;
  --orange-light:#e6964b;
  --seal:#f0c48a;
  --ink:#2f2f2f;
  --muted:#7a7a7a;
  --white:#ffffff;
}
*{margin:0;padding:0;box-sizing:border-box}
html,body{width:679px;height:1200px;overflow:hidden;background:var(--white)}
body{position:relative;font-family:"Open Sans",sans-serif;color:var(--ink)}
.abs{position:absolute}
.head{font-family:"Raleway",sans-serif}

.site-header{position:absolute;left:0;top:0;width:679px;height:53px;background:var(--white)}
.brand{left:106px;top:16px;display:flex;align-items:center;gap:6px;font-family:"Raleway",sans-serif;font-weight:600;font-size:14px;color:var(--teal-dark)}
.brand-dot{width:12px;height:12px;border-radius:50%;background:var(--orange)}
.nav{top:25px;font-size:7.5px;color:#444}
.login{left:518px;top:21px;width:45px;height:17px;background:var(--teal);color:var(--white);font-size:7.5px;text-align:center;line-height:17px}

.hero{left:0;top:53px;width:679px;height:250px;background:linear-gradient(90deg,#e4e4e2,#f1f1ef 40%,#ecebe8 70%,#e2e1de)}
.hero-title{top:78px;width:679px;text-align:center;font-size:19px;color:var(--teal);font-weight:500}
.hero-sub{top:102px;width:679px;text-align:center;font-size:12px;color:#333;font-family:"Raleway",sans-serif}
.hero-video{left:223px;top:137px;width:236px;height:136px;background:linear-gradient(135deg,#c7cfd4,#8a949c 55%,#5d6870);border:1px solid #bbb}
.play{width:30px;height:30px;border-radius:50%;background:var(--white);display:flex;align-items:center;justify-content:center}

.intro-band{left:0;top:303px;width:679px;height:119px;background:linear-gradient(180deg,var(--orange-light),var(--orange))}
.thumb{display:flex;align-items:center;justify-content:center}
.thumb .play{width:20px;height:20px}
.band-title{font-size:11px;color:var(--white);font-weight:500}
.band-copy{font-size:5.6px;line-height:9.8px;color:#fbe3cf;width:110px}

.services-title{top:451px;width:679px;text-align:center;font-size:17px;color:#333}
.services-sub{top:474px;width:679px;text-align:center;font-size:10.5px;color:#333;font-family:"Raleway",sans-serif}
.svc-icon{width:26px;height:26px}
.svc-title{font-size:10px;color:var(--teal);font-family:"Raleway",sans-serif;font-weight:500}
.svc-copy{font-size:5.8px;line-height:9.8px;color:var(--muted);width:150px}

.cta-band{left:0;top:718px;width:679px;height:79px;background:linear-gradient(180deg,var(--teal-light),var(--teal))}
.cta-title{top:736px;width:679px;text-align:center;font-size:18px;color:var(--white)}
.cta-sub{top:760px;width:679px;text-align:center;font-size:10.5px;color:var(--white);font-family:"Raleway",sans-serif}

.guarantee{left:0;top:797px;width:679px;height:190px;background:linear-gradient(180deg,#fafafa,#ececec);border-bottom:1px solid #e2e2e2}
.g-title{left:110px;top:838px;font-size:16px;color:#333}
.g-title b{font-weight:600}
.g-sub{left:110px;top:862px;font-size:9.5px;color:#333;font-family:"Raleway",sans-serif}
.g-copy{left:110px;font-size:5.6px;line-height:9.8px;color:#555;width:268px}
.seal{left:423px;top:839px;width:104px;height:104px;border-radius:50%;background:radial-gradient(circle,#f6d7a8,var(--seal))}

.pkg-title{top:1011px;width:679px;text-align:center;font-size:13.5px;color:var(--teal)}
.pkg-sub{top:1030px;width:679px;text-align:center;font-size:9.5px;color:var(--teal);font-family:"Raleway",sans-serif}
.pkg-head{font-size:7.5px;color:#333;font-weight:400}
.pkg-copy{font-size:5.8px;line-height:9.8px;color:#999;width:110px}

.site-footer{left:0;top:1132px;width:679px;height:68px;background:var(--teal-dark)}
.foot-links{left:110px;top:1152px;font-size:7.5px;color:var(--white);font-family:"Raleway",sans-serif}
.foot-links span{margin:0 4px;color:#9cc}
.legal{left:110px;top:1167px;font-size:6px;color:#9cbcbc}
.social{left:528px;top:1151px;display:flex;gap:6px}
.social i{display:block;width:9px;height:9px;border-radius:50%;background:var(--white)}
</style>
</head>
<body>

<header class="site-header">
  <div class="abs brand"><span class="brand-dot"></span>Rank Ladder Kit</div>
  <a class="abs nav" style="left:358px">Success Stories</a>
  <a class="abs nav" style="left:440px">FAQs</a>
  <a class="abs nav" style="left:484px">Blog</a>
  <a class="abs login">Login</a>
</header>

<section class="abs hero" role="img" aria-label="Soft background photo of a team working in a bright office"></section>
<h1 class="abs hero-title head">Mauris lacus vitae felis vestibulum volutpat</h1>
<p class="abs hero-sub">Sed metus augue convallis et vehicula ut pulvinar eu ante</p>
<svg class="abs" style="left:94px;top:158px" width="18" height="42" viewBox="0 0 18 42"><polyline points="16,1 2,21 16,41" fill="none" stroke="#222" stroke-width="1.2"/></svg>
<svg class="abs" style="left:557px;top:158px" width="18" height="42" viewBox="0 0 18 42"><polyline points="2,1 16,21 2,41" fill="none" stroke="#222" stroke-width="1.2"/></svg>
<div class="abs hero-video thumb" role="img" aria-label="Intro video still of two colleagues at a desk">
  <div class="play"><svg width="12" height="12" viewBox="0 0 12 12"><polygon points="3,1 11,6 3,11" fill="#111"/></svg></div>
</div>

<section class="abs intro-band"></section>
<div class="abs thumb" style="left:110px;top:332px;width:109px;height:68px;background:linear-gradient(135deg,#e9e4df,#b9aca2);border:1px solid #f4d9c0" role="img" aria-label="Video still of a smiling blogger at a laptop">
  <div class="play"><svg width="9" height="9" viewBox="0 0 12 12"><polygon points="3,1 11,6 3,11" fill="#111"/></svg></div>
</div>
<h2 class="abs band-title head" style="left:227px;top:330px">What We Do</h2>
<p class="abs band-copy" style="left:227px;top:347px">Cras a ante vitae enim iaculis aliquam Mauris nunc quam venenatis nec euismod sit amet egestas placerat est Pellentesque habitant morbi tristique senectus et netus et malesuada</p>
<div class="abs thumb" style="left:350px;top:329px;width:109px;height:68px;background:linear-gradient(135deg,#c9c0b6,#7d7670);border:1px solid #f4d9c0" role="img" aria-label="Video still of a team gathered around a laptop">
  <div class="play"><svg width="9" height="9" viewBox="0 0 12 12"><polygon points="3,1 11,6 3,11" fill="#111"/></svg></div>
</div>
<h2 class="abs band-title head" style="left:467px;top:327px">How it Works</h2>
<p class="abs band-copy" style="left:467px;top:344px">Cras a ante vitae enim iaculis aliquam Mauris nunc quam venenatis nec euismod sit amet egestas placerat est Pellentesque habitant morbi tristique senectus et netus et malesuada</p>

<h2 class="abs services-title head" style="font-weight:400">Cum sociis natoque penatibus et magnis</h2>
<p class="abs services-sub">Pellentesque faucibus Ut accumsan ultricies elit Maecenas at justo id velit placerat</p>

<svg class="abs svc-icon" style="left:143px;top:522px" viewBox="0 0 26 26"><rect x="2" y="5" width="17" height="17" rx="2" fill="none" stroke="#d56f27" stroke-width="2"/><path d="M10 16 L22 4 L25 7 L13 19 L9 20 Z" fill="#d56f27"/></svg>
<h3 class="abs svc-title" style="left:181px;top:523px">Featured Service</h3>
<p class="abs svc-copy" style="left:181px;top:539px">Cras a ante vitae enim iaculis aliquam Mauris nunc quam venenatis nec euismod sit amet</p>

<svg class="abs svc-icon" style="left:141px;top:585px" viewBox="0 0 28 26"><rect x="5" y="5" width="18" height="12" fill="none" stroke="#d56f27" stroke-width="2"/><rect x="1" y="19" width="26" height="2" fill="#d56f27"/></svg>
<h3 class="abs svc-title" style="left:181px;top:585px">Featured Service</h3>
<p class="abs svc-copy" style="left:181px;top:601px">Cras a ante vitae enim iaculis aliquam Mauris nunc quam venenatis nec euismod sit amet</p>

<svg class="abs svc-icon" style="left:143px;top:648px" viewBox="0 0 26 26"><polyline points="2,2 2,23 25,23" fill="none" stroke="#d56f27" stroke-width="2"/><polyline points="5,19 11,12 15,16 23,7" fill="none" stroke="#d56f27" stroke-width="2.4"/><polygon points="18,6 24,5 23,11" fill="#d56f27"/></svg>
<h3 class="abs svc-title" style="left:181px;top:647px">Featured Service</h3>
<p class="abs svc-copy" style="left:181px;top:663px">Cras a ante vitae enim iaculis aliquam Mauris nunc quam venenatis nec euismod sit amet</p>

<svg class="abs svc-icon" style="left:379px;top:523px" viewBox="0 0 26 26"><circle cx="13" cy="13" r="12" fill="#d56f27"/><path d="M7 6 Q11 9 9 13 Q13 15 12 20 M16 4 Q15 8 19 10 Q22 13 20 17" fill="none" stroke="#fff" stroke-width="1.6"/></svg>
<h3 class="abs svc-title" style="left:416px;top:522px">Featured Service</h3>
<p class="abs svc-copy" style="left:416px;top:538px">Cras a ante vitae enim iaculis aliquam Mauris nunc quam venenatis nec euismod sit amet</p>

<svg class="abs svc-icon" style="left:381px;top:587px" viewBox="0 0 26 26"><circle cx="13" cy="6" r="4" fill="#d56f27"/><circle cx="5" cy="9" r="3" fill="#d56f27"/><circle cx="21" cy="9" r="3" fill="#d56f27"/><rect x="7" y="12" width="12" height="13" rx="4" fill="#d56f27"/><rect x="0" y="13" width="8" height="9" rx="3" fill="#d56f27"/><rect x="18" y="13" width="8" height="9" rx="3" fill="#d56f27"/></svg>
<h3 class="abs svc-title" style="left:416px;top:584px">Featured Service</h3>
<p class="abs svc-copy" style="left:416px;top:600px">Cras a ante vitae enim iaculis aliquam Mauris nunc quam venenatis nec euismod sit amet</p>

<svg class="abs svc-icon" style="left:382px;top:650px" viewBox="0 0 26 26"><rect x="7" y="1" width="12" height="24" rx="2" fill="none" stroke="#d56f27" stroke-width="2"/><circle cx="13" cy="21" r="1.3" fill="#d56f27"/></svg>
<h3 class="abs svc-title" style="left:416px;top:647px">Featured Service</h3>
<p class="abs svc-copy" style="left:416px;top:663px">Cras a ante vitae enim iaculis aliquam Mauris nunc quam venenatis nec euismod sit amet</p>

<section class="abs cta-band"></section>
<h2 class="abs cta-title head" style="font-weight:400">Proin nulla arcu nonummy luctus dictum</h2>
<p class="abs cta-sub">Pellentesque faucibus Ut accumsan ultricies elitat</p>

<section class="abs guarantee"></section>
<h2 class="abs g-title head" style="font-weight:400"><b>100%</b> Money Back Guarantee</h2>
<p class="abs g-sub">Pellentesque faucibus Ut accumsan ultricies elit Maecenas</p>
<p class="abs g-copy" style="top:882px">Curabitur iaculis tempus eros Curabitur vel mi sit amet magna malesuada ultrices Ut nisi erat fermentum vel congue id euismod in elit Fusce ultricies orci ac feugiat suscipit leo massa sodales velit et scelerisque mi tortor at ipsum cligula augue bibendum accumsan</p>
<p class="abs g-copy" style="top:916px">vestibulum ut commodo a mi Morbi ornare gravida elit Integer congue augue et malesuada iaculis ipsum dui aliquet felis at cursus magna nisl nec elit Praesent elementum elit</p>
<div class="abs seal" role="img" aria-label="Money back guarantee seal"></div>

<h2 class="abs pkg-title head" style="font-weight:400">Get Started Now- Choose an PageForge Package</h2>
<p class="abs pkg-sub">Pellentesque faucibus accumsan ultricies elitat</p>

<svg class="abs" style="left:190px;top:1063px" width="28" height="30" viewBox="0 0 28 30"><rect x="2" y="5" width="24" height="23" rx="2" fill="none" stroke="#d56f27" stroke-width="2.4"/><rect x="2" y="5" width="24" height="5" fill="#d56f27"/><rect x="7" y="1" width="3" height="7" fill="#d56f27"/><rect x="18" y="1" width="3" height="7" fill="#d56f27"/></svg>
<h3 class="abs pkg-head" style="left:225px;top:1064px">Aida elit Integer congue</h3>
<p class="abs pkg-copy" style="left:225px;top:1077px">augue et malesuada iaculis ipsum dui aliquet felis at cursus magna</p>

<svg class="abs" style="left:363px;top:1062px" width="26" height="30" viewBox="0 0 26 30"><path d="M6 13 V9 a7 7 0 0 1 14 0 V13" fill="none" stroke="#d56f27" stroke-width="3"/><rect x="2" y="13" width="22" height="16" rx="2" fill="#d56f27"/></svg>
<h3 class="abs pkg-head" style="left:399px;top:1064px">Aida elit Integer congue</h3>
<p class="abs pkg-copy" style="left:399px;top:1077px">augue et malesuada iaculis ipsum dui aliquet felis at cursus magna</p>

<footer class="abs site-footer"></footer>
<nav class="abs foot-links">About<span>|</span>Success Stories<span>|</span>FAQs<span>|</span>Blog<span>|</span>Support<span>|</span>Contact</nav>
<p class="abs legal">© 2015 Company Name &nbsp;All right reserved &nbsp;Term of Use</p>
<div class="abs social" aria-label="Social links"><i></i><i></i><i></i></div>

</body>
</html>
```